Commercial cleaning business needs a trifold brochure to spotlight janitorial services offered.

Looking for a catchy, creative, trifold brochure to give a description of services offered. This would be used for new potential customers. Our primary colors are royal blue, light gray, and white as included in our logo. The logo does include "restoration", however we only want this brochure to be focused solely on the commercial cleaning side for janitorial services as we already purchased a brochure for the restoration. You can visit our website to get a better idea. www.tvrqservices.example

```html
<!DOCTYPE html>
<html lang="en">
<head>
<meta charset="utf-8">
<title>TVRQ Commercial Cleaning Trifold</title>
<link rel="stylesheet" href="https://fonts.googleapis.com/css2?family=Oswald:wght@400;500&family=Lato:wght@400;700&display=swap">
<style>
:root{
  --royal:#2f2a86;
  --royal-deep:#221e6b;
  --royal-soft:#4a44a8;
  --gray:#b9b9bd;
  --gray-light:#ececee;
  --page:#d6d6d8;
  --white:#ffffff;
  --ink:#555560;
  --photo-warm:#b9aa96;
  --photo-cool:#a9b7c6;
}
*{box-sizing:border-box;margin:0;padding:0}
html,body{width:944px;height:1200px;overflow:hidden;background:var(--page)}
body{position:relative;font-family:"Lato",sans-serif;color:var(--ink)}
.sheet{position:absolute;left:130px;width:646px;height:500px;display:grid;grid-template-columns:repeat(3,1fr);box-shadow:0 14px 14px -8px rgba(0,0,0,.45);background:var(--white);overflow:hidden}
.sheet--outside{top:54px}
.sheet--inside{top:606px}
.panel{position:relative;overflow:hidden}
.layer{position:absolute;inset:0;width:100%;height:100%}
.photo{position:absolute}
.heading{font-family:"Oswald",sans-serif;font-weight:500;color:var(--royal);text-transform:uppercase;line-height:1.05;letter-spacing:-.2px}
.heading--light{color:var(--white)}
.copy{font-size:8.6px;line-height:1.38;text-align:justify}
.copy--light{color:var(--white)}
.center{text-align:center}
.brand{display:flex;flex-direction:column;align-items:center;gap:3px}
.brand__name{display:flex;align-items:center;gap:6px;font-family:"Oswald",sans-serif;font-weight:500;color:var(--royal);letter-spacing:1px}
.brand__dot{border-radius:50%;background:var(--royal)}
.brand__tag{font-family:"Lato",sans-serif;font-weight:700;color:var(--royal)}
.phone-pill{display:flex;align-items:center;justify-content:center;gap:8px;font-family:"Oswald",sans-serif;font-weight:500;border-radius:14px}
.phone-icon{width:12px;height:16px}
</style>
</head>
<body>

<!-- OUTSIDE SPREAD -->
<section class="sheet sheet--outside">

  <!-- Panel: experience -->
  <article class="panel">
    <div class="photo" role="img" aria-label="Worker polishing an office floor with a buffing machine" style="left:0;top:0;width:100%;height:230px;background:linear-gradient(160deg,#d9cdb9,#a89880 60%,#6d84a2)"></div>
    <svg class="layer" viewBox="0 0 215 500" preserveAspectRatio="none">
      <path d="M0 205 Q110 175 215 170 L215 500 L0 500Z" fill="var(--royal)"/>
      <path d="M0 222 Q110 190 215 182 L215 500 L0 500Z" fill="var(--gray)"/>
      <path d="M0 236 Q110 203 215 194 L215 500 L0 500Z" fill="var(--white)"/>
      <path d="M0 418 Q100 412 215 398 L215 500 L0 500Z" fill="var(--royal)"/>
      <path d="M0 418 Q60 415 110 408 L0 470Z" fill="var(--royal-soft)" opacity=".6"/>
    </svg>
    <h2 class="heading" style="position:absolute;left:12px;top:228px;font-size:16.5px">Experience<br>High-Tech Efficiency</h2>
    <div style="position:absolute;left:14px;top:268px;width:192px">
      <p class="copy">Tri-Valley Regional Quality Maintenance follows a technology-based service delivery process. In our company, employees communicate with each other using smartphone/tablet apps so that they can track every cleaning team's whereabouts.</p>
      <p class="copy" style="margin-top:8px">This enables main office managers to efficiently monitor work progress in real time. With this high-tech infrastructure in place, our cleaners can be able to relay on-the-spot customer requests to us immediately. We can then issue instructions just as quickly to employees on site.</p>
    </div>
    <p class="copy--light center" style="position:absolute;left:0;right:0;top:456px;font-size:9.4px;line-height:1.65;letter-spacing:.4px;color:var(--white)">It's not just about cleaning,<br>it's about the communication</p>
  </article>

  <!-- Panel: contact -->
  <article class="panel">
    <svg class="layer" viewBox="0 0 215 500" preserveAspectRatio="none">
      <path d="M0 0 H215 V125 Q110 130 0 150Z" fill="var(--royal)"/>
      <path d="M0 150 Q110 130 215 125 V132 Q110 138 0 160Z" fill="var(--gray)"/>
      <path d="M0 388 Q110 360 215 356 V500 H0Z" fill="var(--royal)"/>
      <path d="M0 380 Q110 352 215 348 V356 Q110 360 0 388Z" fill="var(--gray)"/>
    </svg>
    <div class="photo" role="img" aria-label="Cleaner mopping a hallway" style="left:46px;top:33px;width:124px;height:124px;border-radius:50%;border:3px solid var(--white);box-shadow:0 0 0 1px var(--gray);background:radial-gradient(circle at 40% 40%,#c7d7e6,#7d93b0 70%,#4b5e82)"></div>
    <h2 class="heading center" style="position:absolute;left:0;right:0;top:168px;font-size:18px">Contact Us</h2>
    <p class="copy center" style="position:absolute;left:14px;right:14px;top:194px;font-size:9.6px;text-align:center;line-height:1.35">Get in touch with us to order janitorial supplies for your offices. You may speak to any of our sales staff to inquire about the range of products we have and their corresponding prices.</p>
    <p class="copy center" style="position:absolute;left:14px;right:14px;top:270px;font-size:9.6px;text-align:center;line-height:1.35">We serve clients all throughout Central and Eastern Kentucky.</p>
    <div class="brand" style="position:absolute;left:0;right:0;top:318px">
      <span class="brand__name" style="font-size:22px"><span class="brand__dot" style="width:10px;height:10px"></span>TVRQ</span>
      <span class="brand__tag" style="font-size:6px">Commercial Cleaning</span>
    </div>
    <div style="position:absolute;left:0;right:0;top:396px;display:flex;justify-content:center;gap:9px">
      <span style="width:15px;height:15px;border:1px solid var(--white);border-radius:50%"></span>
      <span style="width:15px;height:15px;border:1px solid var(--white);border-radius:50%"></span>
      <span style="width:15px;height:15px;border:1px solid var(--white);border-radius:50%"></span>
    </div>
    <h2 class="heading heading--light center" style="position:absolute;left:0;right:0;top:416px;font-size:18.5px;font-weight:400">Free Quote or Estimate!</h2>
    <p class="center" style="position:absolute;left:0;right:0;top:447px;font-size:9.6px;line-height:1.62;color:var(--white);letter-spacing:.4px">1-866-555-0142<br>sales@tvrqservices.example<br>www.tvrqservices.example</p>
  </article>

  <!-- Panel: cover -->
  <article class="panel">
    <div class="photo" role="img" aria-label="Smiling cleaning staff in blue uniforms wiping office desks" style="left:0;top:120px;width:100%;height:260px;background:linear-gradient(135deg,#e3e1de,#b5c1d0 45%,#5f7fb8 75%,#c9c6c0)"></div>
    <svg class="layer" viewBox="0 0 215 500" preserveAspectRatio="none">
      <path d="M0 115 Q110 120 215 130 V0 H0Z" fill="var(--white)"/>
      <path d="M0 118 Q110 124 215 134 V127 Q110 117 0 112Z" fill="var(--royal)"/>
      <path d="M0 360 Q110 350 215 356 V500 H0Z" fill="var(--royal)"/>
      <path d="M0 352 Q110 342 215 348 V356 Q110 350 0 360Z" fill="var(--gray)"/>
    </svg>
    <div class="brand" style="position:absolute;left:0;right:0;top:38px">
      <span class="brand__name" style="font-size:34px"><span class="brand__dot" style="width:14px;height:14px"></span>TVRQ</span>
      <span class="brand__tag" style="font-size:9px">Commercial Cleaning</span>
    </div>
    <h1 class="heading heading--light center" style="position:absolute;left:0;right:0;top:380px;font-size:24px;font-weight:400">Commercial Cleaning</h1>
    <p class="center" style="position:absolute;left:0;right:0;top:418px;font-size:10px;color:var(--gray-light)">Experience High-Tech Efficiency</p>
    <div class="phone-pill" style="position:absolute;left:20px;width:180px;top:438px;height:28px;background:var(--gray-light);color:var(--royal);font-size:18px">
      <svg class="phone-icon" viewBox="0 0 12 16"><rect x="1" y="1" width="10" height="14" rx="2" fill="none" stroke="var(--royal)" stroke-width="2"/><rect x="4" y="11" width="4" height="1.6" fill="var(--royal)"/></svg>
      1-866-555-0142
    </div>
    <p class="center" style="position:absolute;left:0;right:0;top:476px;font-size:10px;letter-spacing:.8px;color:var(--white)">www.tvrqservices.example</p>
  </article>
</section>

<!-- INSIDE SPREAD -->
<section class="sheet sheet--inside">

  <!-- Panel: about -->
  <article class="panel" style="background:var(--royal)">
    <div class="photo" role="img" aria-label="Cleaner wiping a boardroom table with microphones" style="left:0;top:0;width:100%;height:215px;background:linear-gradient(150deg,#c7c9d0,#8a6a4e 45%,#3e3e44 80%,#5a5a62)"></div>
    <svg class="layer" viewBox="0 0 215 500" preserveAspectRatio="none">
      <path d="M0 200 Q100 185 215 195 V220 Q100 205 0 240Z" fill="var(--gray)"/>
      <path d="M0 212 Q100 196 215 204 V226 Q100 215 0 250Z" fill="var(--white)"/>
      <path d="M0 250 Q100 215 215 226 V500 H0Z" fill="var(--royal)"/>
    </svg>
    <h2 class="heading heading--light" style="position:absolute;left:15px;top:258px;font-size:18px">About Us</h2>
    <div style="position:absolute;left:15px;top:288px;width:190px">
      <p class="copy copy--light" style="font-size:9px">Tri-Valley Regional Quality Maintenance is committed to providing an unsurpassed level of janitorial services and building long-lasting relationships with clients. We accomplish this by using modern technology to communicate effectively with client's and employees.</p>
      <p class="copy copy--light" style="font-size:9px;margin-top:13px">Our team leaders assist clients in defining their needs and communicate those needs to our employees. We act with integrity in all aspects of our business at all times. Our goal is to deliver a consistently high level of janitorial services that are within your budget.</p>
    </div>
  </article>

  <!-- Panel: services -->
  <article class="panel" style="background:linear-gradient(90deg,var(--white) 70%,var(--gray-light))">
    <div class="brand" style="position:absolute;left:0;right:0;top:40px">
      <span class="brand__name" style="font-size:30px"><span class="brand__dot" style="width:12px;height:12px"></span>TVRQ</span>
      <span class="brand__tag" style="font-size:8px">Commercial Cleaning</span>
    </div>
    <h2 class="heading center" style="position:absolute;left:0;right:0;top:111px;font-size:18px">Our Services</h2>
    <p class="copy" style="position:absolute;left:10px;right:10px;top:140px;font-size:9.2px;text-align:left">Our company specializes in cleaning medical facilities and class-A office spaces. You can contact us to request:</p>
    <div style="position:absolute;left:0;right:0;top:200px;display:flex;justify-content:space-around;padding:0 6px">
      <figure class="center"><div role="img" aria-label="Carpet cleaning icon" style="width:46px;height:46px;margin:0 auto;border-radius:50%;background:var(--royal);box-shadow:0 0 0 2px var(--gray-light),0 0 0 3px var(--gray)"></div><figcaption style="font-size:7px;margin-top:8px">Carpet Cleaning</figcaption></figure>
      <figure class="center"><div role="img" aria-label="Floor care icon" style="width:46px;height:46px;margin:0 auto;border-radius:50%;background:var(--royal);box-shadow:0 0 0 2px var(--gray-light),0 0 0 3px var(--gray)"></div><figcaption style="font-size:7px;margin-top:8px">Floor Care</figcaption></figure>
      <figure class="center"><div role="img" aria-label="Janitorial services icon" style="width:46px;height:46px;margin:0 auto;border-radius:50%;background:var(--royal);box-shadow:0 0 0 2px var(--gray-light),0 0 0 3px var(--gray)"></div><figcaption style="font-size:7px;margin-top:8px">Janitorial Services</figcaption></figure>
    </div>
    <div style="position:absolute;left:0;right:0;top:274px;display:flex;justify-content:center;gap:24px">
      <figure class="center"><div role="img" aria-label="Window cleaning icon" style="width:46px;height:46px;margin:0 auto;border-radius:50%;background:var(--royal);box-shadow:0 0 0 2px var(--gray-light),0 0 0 3px var(--gray)"></div><figcaption style="font-size:7px;margin-top:8px;line-height:1.4">Window<br>Cleaning</figcaption></figure>
      <figure class="center"><div role="img" aria-label="24-hour emergency water extraction icon" style="width:46px;height:46px;margin:0 auto;border-radius:50%;background:var(--royal);box-shadow:0 0 0 2px var(--gray-light),0 0 0 3px var(--gray)"></div><figcaption style="font-size:7px;margin-top:8px;line-height:1.4">24- Hour Emergency<br>Water Extraction Services</figcaption></figure>
    </div>
    <div class="photo" role="img" aria-label="Hand cleaning a surface" style="left:3px;top:373px;width:76px;height:76px;border-radius:50%;border:2px solid var(--white);background:radial-gradient(circle,#d4d8dd,#8b96a4)"></div>
    <div class="photo" role="img" aria-label="Hotel housekeeping staff member with cart" style="left:135px;top:373px;width:76px;height:76px;border-radius:50%;border:2px solid var(--white);background:radial-gradient(circle,#e2e3e6,#8d8f95)"></div>
    <div class="photo" role="img" aria-label="Housekeeper in uniform" style="left:64px;top:366px;width:86px;height:86px;border-radius:50%;border:3px solid var(--white);background:radial-gradient(circle,#e6c9a5,#8a4f2a 75%);box-shadow:0 2px 4px rgba(0,0,0,.3)"></div>
    <div class="phone-pill" style="position:absolute;left:8px;right:22px;top:462px;height:28px;background:var(--royal);color:var(--white);font-size:19px;box-shadow:0 0 0 2px var(--gray-light),0 0 0 3px var(--gray)">
      <svg class="phone-icon" viewBox="0 0 12 16"><rect x="1" y="1" width="10" height="14" rx="2" fill="none" stroke="var(--white)" stroke-width="2"/><rect x="4" y="11" width="4" height="1.6" fill="var(--white)"/></svg>
      1-866-555-0142
    </div>
  </article>

  <!-- Panel: inspect -->
  <article class="panel">
    <div class="photo" role="img" aria-label="Cleaner mopping an office floor next to a wet floor sign" style="left:0;top:320px;width:100%;height:180px;background:linear-gradient(180deg,#dfe3e8,#a7b4c4 60%,#c7c2b4)"></div>
    <svg class="layer" viewBox="0 0 215 500" preserveAspectRatio="none">
      <path d="M0 0 H215 V320 Q110 295 0 320Z" fill="var(--royal)"/>
      <path d="M0 320 Q110 295 215 320 V340 Q110 312 0 332Z" fill="var(--white)"/>
      <path d="M0 332 Q110 312 215 340 V348 Q110 320 0 340Z" fill="var(--gray)"/>
    </svg>
    <h2 class="heading heading--light" style="position:absolute;left:14px;top:40px;font-size:18px;font-weight:400">We Inspect Our Work</h2>
    <ul style="position:absolute;left:14px;width:190px;top:80px;list-style:none">
      <li style="display:flex;gap:7px;margin-bottom:14px"><span style="flex:none;width:8px;height:8px;margin-top:2px;border-radius:50%;background:var(--gray)"></span><p class="copy copy--light" style="font-size:9px">We focus on our cleaners so that they can focus on you. Finding the perfect cleaner can be a real challenge.</p></li>
      <li style="display:flex;gap:7px;margin-bottom:14px"><span style="flex:none;width:8px;height:8px;margin-top:2px;border-radius:50%;background:var(--gray)"></span><p class="copy copy--light" style="font-size:9px">It's not just about cleaning, it's about communication. TVRQ recognizes that doing a great job is more than just providing great cleaning.</p></li>
      <li style="display:flex;gap:7px"><span style="flex:none;width:8px;height:8px;margin-top:2px;border-radius:50%;background:var(--gray)"></span><p class="copy copy--light" style="font-size:9px">No cleaning company cares more about quality, and we can prove it. From the technology we use, to our quality inspections, we invest heavily in making sure that we are providing you the best possible cleaning services.</p></li>
    </ul>
  </article>
</section>

</body>
</html>
```